Flyer für IT-Firma
Zielgruppe
Wir sind eine IT-Firma, die sich unter anderem auf IT-Netzwerke spezialisiert hat. Wir verkaufen Netzwerklösungen, aber auch Produkte im Bereich IT Netzwerk, IT Security, WLAN, Cloud-Lösungen, etc. und Services. Unsere Zielgruppen für diesen Bereich sind kleinere bis Mittlere Unternehmen aber auch öffentliche Verwaltungen, Schulen, Spitäler etc. die ihre IT Netzwerke verbessern möchten und sich absichern möchten für den Fall von WLAN Ausfall oder Datenverlust. Diese Zielgruppen kennen uns womöglich noch nicht oder haben in einem anderen Projekt mit uns zusammengearbeitet. Der Flyer soll sie also von uns und dem Produkt überzeugen.
Aufgabenstellung
Der Flyer soll 2-Seitig oder 4-Seitig sein. Er soll als Vorlage für die Präsentation verschiedenster Produkte dienen. Ziel ist es einen Flyer zu haben im einheitlichen Design, den wir beliebig mit Fotos und Text abfüllen können. So dass wir unsere Produkte und Dienstleistungen im einheitlichen Design vorstellen können. Der Flyer soll folgende Elemente beinhalten:
Seite 1 eher oberflächlich das Produkt vorstellen
- Logo
- Einleitung zum Unternehmen und oder Produkt
- 1-2 Platzhalter für Bilder
- Weiterer Text für Produktbeschreibung
Seite 2 detaillierte Informationen:
- technische Daten (allenfalls in Listenform)
- Weitere Detailinformationen
- Preise
- Kontakt
Vorzugsweise Format A4 damit man auch daraus einfach ein PDF generieren kann und per Mail versenden kann. Vorschläge für andere Formate sind willkommen.

```html
<!DOCTYPE html>
<html lang="de">
<head>
<meta charset="utf-8">
<title>Netaris Flyer</title>
<link href="https://fonts.googleapis.com/css2?family=Lato:wght@400;700;900&display=swap" rel="stylesheet">
<style>
:root{
  --teal:#146a7a;
  --orange:#f59a2b;
  --green:#6aac46;
  --sky:#e4f2fb;
  --sky-line:#cfe6f4;
  --ink:#2b2b2b;
  --brand-grey:#555555;
  --stage:#e6e6e6;
}
*{margin:0;padding:0;box-sizing:border-box}
html,body{width:960px;height:1200px;overflow:hidden}
body{background:var(--stage);font-family:'Lato',sans-serif;color:var(--ink);position:relative}
.page{position:absolute;width:369px;height:522px;background:#fff;overflow:hidden}
.p1{left:102px;top:70px}.p2{left:489px;top:70px}.p3{left:102px;top:608px}.p4{left:489px;top:608px}
.abs{position:absolute}
.brand{position:absolute;left:0;right:0;text-align:center;line-height:1;font-weight:700;color:var(--brand-grey)}
.photo{position:absolute;border:4px solid #fff;border-radius:14px;box-shadow:0 1px 4px rgba(0,0,0,.15)}
.web{position:absolute;left:0;right:0;text-align:center;color:#fff;font-size:12px;letter-spacing:3px}
.txt{font-size:7.6px;line-height:1.28}
.card{position:absolute;border-radius:12px;color:#fff;padding:0 17px}
.card .kicker{font-size:6.2px;font-weight:700}
.card h3{font-size:13px;font-weight:700;margin-top:1px}
.card .rule{width:34px;height:1px;background:#fff;margin:5px 0 7px}
.card p{font-size:7.3px;line-height:1.14}
.data{position:absolute;left:26px;top:97px;width:317px;height:162px;border:2px solid var(--green);border-radius:9px;padding:4px 5px}
.data table{width:100%;border-collapse:separate;border-spacing:1px 0;font-size:5.8px;text-align:center}
.data th{background:var(--orange);color:#fff;font-weight:700;font-size:7px;height:15px}
.data td{height:13.3px;color:#333}
.data tr:nth-child(even) td{background:#eef3f5}
.price{position:absolute;width:155px;height:57px;border:2px solid var(--sky-line);border-radius:7px;background:#fff;padding:7px 11px}
.price .row{display:flex;justify-content:space-between;font-size:10.5px;font-weight:700}
.price .row span:first-child{color:var(--teal)}
.price .row span:last-child{color:var(--orange)}
.price p{font-size:5.6px;line-height:1.22;margin-top:4px}
.steps{position:absolute;left:199px;top:172px;width:160px;list-style:none}
.steps li{display:flex;gap:6px;margin-bottom:9.5px}
.steps b{color:var(--teal);font-size:10px;width:8px}
.steps span{font-size:6.5px;line-height:1.25}
.tick{position:absolute;width:162px;color:#fff}
.tick .head{display:flex;align-items:center;gap:8px}
.tick h4{font-size:13px;font-weight:400;line-height:1.05}
.tick p{font-size:6.5px;line-height:1.2;margin-top:4px}
.contact{position:absolute;color:#fff;font-size:10px;line-height:16px}
.contact div{display:flex;align-items:center;gap:6px}
</style>
</head>
<body>

<!-- Seite 1 -->
<section class="page p1">
  <svg class="abs" style="left:0;top:0" width="369" height="522" aria-hidden="true">
    <path d="M0 170 Q185 215 369 170 V522 H0Z" fill="var(--sky)"/>
    <path d="M0 470 Q185 400 369 470 V522 H0Z" fill="var(--teal)"/>
  </svg>
  <div class="brand" style="top:22px;font-size:23px">Netaris</div>
  <div class="abs" style="left:0;right:0;top:58px;text-align:center;font-weight:900;font-size:34px;line-height:31px"><span style="color:var(--teal)">LOREM IPSUM</span><br><span style="color:var(--orange)">DOLOR SITAMET</span></div>
  <div class="abs" style="left:84px;top:128px;width:202px;height:21px;background:var(--green);border-radius:3px;color:#fff;font-size:13px;text-align:center;line-height:21px">Lorem ipsum dolor sit amet</div>
  <p class="abs txt" style="left:40px;right:40px;top:157px;text-align:center;font-size:7.9px">Lorem ipsum dolor sit amet, consectetur adipiscing elit, sed do eiusmod tempor incididunt ut labore et dolore magna aliqua. Ut enim ad minim veniam, quis nostrud exercitation ullamco laboris nisi ut aliquip ex ea commodo consequat.</p>
  <div class="card" style="left:29px;top:312px;width:150px;height:167px;background:var(--orange)">
    <div class="kicker" style="margin-top:34px">Lorem ipsum dolor sit amet</div><h3>Lorem ipsum dolor</h3><div class="rule"></div>
    <p>Lorem ipsum dolor sit amet, consectetur adipiscing elit, sed do eiusmod tempor incididunt ut labore et dolore magna aliqua. Ut enim ad minim veniam, quis nostrud exercitation ullamco laboris nisi ut aliquip ex ea commodo consequat. Duis aute irure dolor in reprehenderit in voluptate velit esse cillum dolore eu fugiat nulla pariatur.</p>
  </div>
  <div class="card" style="left:189px;top:312px;width:151px;height:167px;background:var(--green)">
    <div class="kicker" style="margin-top:34px">Lorem ipsum dolor sit amet</div><h3>Lorem ipsum dolor</h3><div class="rule"></div>
    <p>Lorem ipsum dolor sit amet, consectetur adipiscing elit, sed do eiusmod tempor incididunt ut labore et dolore magna aliqua. Ut enim ad minim veniam, quis nostrud exercitation ullamco laboris nisi ut aliquip ex ea commodo consequat. Duis aute irure dolor in reprehenderit in voluptate velit esse cillum dolore eu fugiat nulla pariatur.</p>
  </div>
  <div class="photo" role="img" aria-label="Netzwerk-Switch mit Patchkabeln" style="left:29px;top:196px;width:150px;height:134px;background:linear-gradient(135deg,#1c3f66,#3b77a8 55%,#9fb9c8)"></div>
  <div class="photo" role="img" aria-label="Hände an einem Laptop mit farbigen Datenströmen" style="left:189px;top:196px;width:151px;height:134px;background:linear-gradient(135deg,#0d1b3a,#3a2a66 50%,#b0447a 80%,#e0a03a)"></div>
  <div class="web" style="top:490px">www.netaris.ch</div>
</section>

<!-- Seite 2 -->
<section class="page p2">
  <svg class="abs" style="left:0;top:0" width="369" height="522" aria-hidden="true">
    <path d="M0 78 Q185 125 369 60 V522 H0Z" fill="var(--sky)"/>
    <path d="M0 120 Q185 160 369 120 V330 Q185 300 0 330Z" fill="#fff"/>
    <path d="M0 345 H369 V500 H0Z" fill="#fff"/>
    <path d="M30 522 Q185 470 340 522Z" fill="var(--teal)"/>
  </svg>
  <div class="brand" style="top:30px;font-size:27px">Netaris</div>
  <h2 class="abs" style="left:0;right:0;top:73px;text-align:center;color:var(--teal);font-size:16.5px;font-weight:700">Technische Daten</h2>
  <div class="data">
    <table>
      <tr><th>Information</th><th>Lorem ipsum</th><th>Lorem ipsum</th><th>Lorem ipsum</th></tr>
      <tr><td>Lorem ipsum dolor</td><td>Lorem ipsum</td><td>Lorem ipsum</td><td>Lorem ipsum</td></tr>
      <tr><td>Lorem ipsum dolor</td><td>Lorem ipsum</td><td>Lorem ipsum</td><td>Lorem ipsum</td></tr>
      <tr><td>Lorem ipsum dolor</td><td>Lorem ipsum</td><td>Lorem ipsum</td><td>Lorem ipsum</td></tr>
      <tr><td>Lorem ipsum dolor</td><td>Lorem ipsum</td><td>Lorem ipsum</td><td>Lorem ipsum</td></tr>
      <tr><td>Lorem ipsum dolor</td><td>Lorem ipsum</td><td>Lorem ipsum</td><td>Lorem ipsum</td></tr>
      <tr><td>Lorem ipsum dolor</td><td>Lorem ipsum</td><td>Lorem ipsum</td><td>Lorem ipsum</td></tr>
      <tr><td>Lorem ipsum dolor</td><td>Lorem ipsum</td><td>Lorem ipsum</td><td>Lorem ipsum</td></tr>
      <tr><td>Lorem ipsum dolor</td><td>Lorem ipsum</td><td>Lorem ipsum</td><td>Lorem ipsum</td></tr>
      <tr><td>Lorem ipsum dolor</td><td>Lorem ipsum</td><td>Lorem ipsum</td><td>Lorem ipsum</td></tr>
      <tr><td>Lorem ipsum dolor</td><td>Lorem ipsum</td><td>Lorem ipsum</td><td>Lorem ipsum</td></tr>
    </table>
  </div>
  <div class="abs" style="left:0;top:281px;width:63px;height:2px;background:var(--green)"></div>
  <div class="abs" style="left:306px;top:281px;width:63px;height:2px;background:var(--orange)"></div>
  <h2 class="abs" style="left:0;right:0;top:271px;text-align:center;color:var(--teal);font-size:16px;font-weight:700">Weitere Detailinformationen</h2>
  <p class="abs txt" style="left:38px;right:38px;top:295px;text-align:center;font-size:7.6px;line-height:1.27">Lorem ipsum dolor sit amet, consectetur adipiscing elit, sed do eiusmod tempor incididunt ut labore et dolore magna aliqua. Ut enim ad minim veniam, quis nostrud exercitation ullamco laboris nisi ut aliquip ex ea commodo consequat. Duis aute irure dolor in reprehenderit in voluptate velit esse cillum dolore eu</p>
  <div class="abs" style="left:26px;top:349px;width:317px;height:20px;background:var(--green);border-radius:3px;color:#fff;text-align:center;font-size:12px;font-weight:700;line-height:20px">Preise</div>
  <div class="price" style="left:26px;top:378px"><div class="row"><span>Lorem ipsum</span><span>$0.0</span></div><p>Lorem ipsum dolor sit amet, consectetur adipiscing elit, sed do eiusmod tempor incididunt ut labore et dolore magna aliqua.</p></div>
  <div class="price" style="left:188px;top:378px"><div class="row"><span>Lorem ipsum</span><span>$0.0</span></div><p>Lorem ipsum dolor sit amet, consectetur adipiscing elit, sed do eiusmod tempor incididunt ut labore et dolore magna aliqua.</p></div>
  <div class="price" style="left:26px;top:442px"><div class="row"><span>Lorem ipsum</span><span>$0.0</span></div><p>Lorem ipsum dolor sit amet, consectetur adipiscing elit, sed do eiusmod tempor incididunt ut labore et dolore magna aliqua.</p></div>
  <div class="price" style="left:188px;top:442px"><div class="row"><span>Lorem ipsum</span><span>$0.0</span></div><p>Lorem ipsum dolor sit amet, consectetur adipiscing elit, sed do eiusmod tempor incididunt ut labore et dolore magna aliqua.</p></div>
</section>

<!-- Seite 3 -->
<section class="page p3">
  <svg class="abs" style="left:0;top:0" width="369" height="522" aria-hidden="true">
    <path d="M184 170 Q184 155 199 155 H369 V382 H199 Q184 382 184 367Z" fill="var(--sky)"/>
    <path d="M0 478 Q185 400 369 478 V522 H0Z" fill="var(--sky)"/>
    <path d="M0 490 Q185 420 369 490 V522 H0Z" fill="var(--teal)"/>
  </svg>
  <div class="photo" role="img" aria-label="Hand berührt eine IoT-Oberfläche mit Symbolen" style="left:25px;top:19px;width:145px;height:128px;background:linear-gradient(135deg,#2b4f6e,#6a94b4 55%,#b7cfdf)"></div>
  <div class="abs" style="left:201px;top:22px;width:148px;height:20px;background:var(--green);border-radius:3px;color:#fff;text-align:center;font-size:13px;line-height:20px">Lorem ipsum dolor</div>
  <div class="abs txt" style="left:201px;top:50px;width:155px">
    <p>Lorem ipsum dolor sit amet, consectetur adipiscing elit, sed do eiusmod tempor incididunt ut labore et dolore magna aliqua.</p>
    <p style="margin-top:8px">Lorem ipsum dolor sit amet, consectetur adipiscing elit, sed do eiusmod tempor incididunt ut labore et dolore magna aliqua. Ut enim ad minim veniam, quis nostrud exercitation ullamco laboris nisi ut aliquip ex ea commodo consequat.</p>
  </div>
  <h3 class="abs" style="left:28px;top:163px;color:var(--teal);font-size:13.5px;font-weight:700">Lorem ipsum dolor</h3>
  <div class="abs" style="left:28px;top:183px;width:32px;height:1.5px;background:var(--green)"></div>
  <div class="abs txt" style="left:28px;top:194px;width:150px">
    <p>Lorem ipsum dolor sit amet, consectetur adipiscing elit, sed do eiusmod tempor incididunt ut labore et dolore magna aliqua. Ut enim ad minim veniam, quis nostrud exercitation ullamco laboris nisi ut aliquip ex ea commodo consequat.</p>
    <p style="margin-top:8px">Lorem ipsum dolor sit amet, consectetur adipiscing elit, sed do eiusmod tempor incididunt ut labore et dolore magna aliqua. Ut enim ad minim veniam, quis nostrud exercitation ullamco laboris nisi ut aliquip ex ea commodo consequat. Duis aute irure dolor in reprehenderit in voluptate velit esse cillum dolore eu fugiat nulla pariatur. Excepteur sint occaecat cupidatat non proident, sunt in culpa qui officia deserunt mollit anim id est laborum.</p>
    <p style="margin-top:8px">Lorem ipsum dolor sit amet, consectetur adipiscing elit, sed do eiusmod tempor incididunt ut labore et dolore magna aliqua. Ut enim ad minim veniam, quis nostrud exercitation ullamco laboris nisi ut aliquip ex ea commodo consequat.</p>
  </div>
  <ol class="steps">
    <li><b>1.</b><span>Lorem ipsum dolor sit amet, consectetur adipiscing elit, sed do eiusmod tempor incididunt ut labore et dolore magna aliqua.</span></li>
    <li><b>2.</b><span>Lorem ipsum dolor sit amet, consectetur adipiscing elit, sed do eiusmod tempor incididunt ut labore et dolore magna aliqua.</span></li>
    <li><b>3.</b><span>Lorem ipsum dolor sit amet, consectetur adipiscing elit, sed do eiusmod tempor incididunt ut labore et dolore magna aliqua.</span></li>
    <li><b>4.</b><span>Lorem ipsum dolor sit amet, consectetur adipiscing elit, sed do eiusmod tempor incididunt ut labore et dolore magna aliqua.</span></li>
  </ol>
  <div class="photo" role="img" aria-label="Laptop mit schwebenden Diagramm- und App-Symbolen" style="left:204px;top:316px;width:142px;height:127px;background:linear-gradient(135deg,#1d2a3a,#3d5f80 55%,#8aa7bf)"></div>
  <div class="web" style="top:497px">www.netaris.ch</div>
</section>

<!-- Seite 4 -->
<section class="page p4">
  <svg class="abs" style="left:0;top:0" width="369" height="522" aria-hidden="true">
    <rect width="369" height="440" fill="var(--sky)"/>
    <path d="M0 442 Q185 400 369 442 V522 H0Z" fill="var(--teal)"/>
    <line x1="179" y1="468" x2="179" y2="503" stroke="#3f8a98" stroke-width="1"/>
  </svg>
  <h2 class="abs" style="left:31px;top:17px;color:var(--teal);font-size:18px;font-weight:700">Lorem ipsum dolor</h2>
  <div class="abs" style="left:193px;top:30px;width:144px;height:1.5px;background:var(--orange)"></div>
  <p class="abs txt" style="left:31px;top:47px;width:310px;font-size:7.9px">Lorem ipsum dolor sit amet, consectetur adipiscing elit, sed do eiusmod tempor incididunt ut labore et dolore magna aliqua. Ut enim ad minim veniam, quis nostrud exercitation ullamco laboris nisi ut aliquip ex ea commodo consequat. Duis aute irure dolor in reprehenderit in voluptate velit esse cillum dolore eufugiat nulla pariatur. Excepteur sint occaecat cupidatat non proident, sunt in culpa qui officia deserunt mollit anim id est laborum.</p>
  <div class="abs" style="left:13px;top:114px;width:343px;height:220px;background:var(--green);border-radius:18px"></div>
  <h2 class="abs" style="left:31px;top:124px;color:#fff;font-size:18px;font-weight:400">Lorem ipsum dolor</h2>
  <p class="abs txt" style="left:32px;top:150px;width:310px;color:#fff;font-size:7.6px">Lorem ipsum dolor sit amet, consectetur adipiscing elit, sed do eiusmod tempor incididunt ut labore et dolore magna aliqua. Ut enim ad minim veniam, quis nostrud exercitation ullamco laboris nisi ut aliquip ex ea commodo consequat.</p>
  <div class="tick" style="left:34px;top:188px"><div class="head"><svg width="33" height="33" aria-hidden="true"><circle cx="16.5" cy="16.5" r="15" fill="var(--orange)" stroke="#fff" stroke-width="2"/><path d="M10 17 l4.5 4.5 L23 12" fill="none" stroke="#fff" stroke-width="3" stroke-linecap="round" stroke-linejoin="round"/></svg><h4>Lorem ipsum<br>dolor sit amet</h4></div><p>Lorem ipsum dolor sit amet, consectetur adipiscing elit, sed do eiusmod tempor incididunt ut labore et dolore magna aliqua.</p></div>
  <div class="tick" style="left:197px;top:188px"><div class="head"><svg width="33" height="33" aria-hidden="true"><circle cx="16.5" cy="16.5" r="15" fill="var(--orange)" stroke="#fff" stroke-width="2"/><path d="M10 17 l4.5 4.5 L23 12" fill="none" stroke="#fff" stroke-width="3" stroke-linecap="round" stroke-linejoin="round"/></svg><h4>Lorem ipsum<br>dolor sit amet</h4></div><p>Lorem ipsum dolor sit amet, consectetur adipiscing elit, sed do eiusmod tempor incididunt ut labore et dolore magna aliqua.</p></div>
  <div class="tick" style="left:34px;top:256px"><div class="head"><svg width="33" height="33" aria-hidden="true"><circle cx="16.5" cy="16.5" r="15" fill="var(--orange)" stroke="#fff" stroke-width="2"/><path d="M10 17 l4.5 4.5 L23 12" fill="none" stroke="#fff" stroke-width="3" stroke-linecap="round" stroke-linejoin="round"/></svg><h4>Lorem ipsum<br>dolor sit amet</h4></div><p>Lorem ipsum dolor sit amet, consectetur adipiscing elit, sed do eiusmod tempor incididunt ut labore et dolore magna aliqua.</p></div>
  <div class="tick" style="left:197px;top:256px"><div class="head"><svg width="33" height="33" aria-hidden="true"><circle cx="16.5" cy="16.5" r="15" fill="var(--orange)" stroke="#fff" stroke-width="2"/><path d="M10 17 l4.5 4.5 L23 12" fill="none" stroke="#fff" stroke-width="3" stroke-linecap="round" stroke-linejoin="round"/></svg><h4>Lorem ipsum<br>dolor sit amet</h4></div><p>Lorem ipsum dolor sit amet, consectetur adipiscing elit, sed do eiusmod tempor incididunt ut labore et dolore magna aliqua.</p></div>
  <div class="photo" role="img" aria-label="Hände um einen leuchtenden Globus" style="left:20px;top:341px;width:110px;height:100px;border-width:3px;border-radius:10px;background:linear-gradient(135deg,#a9c6de,#3b6f9f 55%,#1c3556)"></div>
  <div class="photo" role="img" aria-label="Hand mit vernetzten Lieferketten-Symbolen" style="left:128px;top:341px;width:110px;height:100px;border-width:3px;border-radius:10px;background:linear-gradient(135deg,#10243c,#2a5d8a 55%,#6ea0c4)"></div>
  <div class="photo" role="img" aria-label="Leuchtendes Cloud-Symbol mit Schaltkreis" style="left:236px;top:341px;width:112px;height:100px;border-width:3px;border-radius:10px;background:radial-gradient(circle at 55% 45%,#2f7fd0,#0f2540 60%,#0a1626)"></div>
  <div class="contact" style="left:59px;top:459px">
    <div><svg width="8" height="8" aria-hidden="true"><circle cx="4" cy="4" r="4" fill="var(--orange)"/><path d="M2.6 2.2 q.2 2.6 2.9 3.6" stroke="#fff" stroke-width="1" fill="none"/></svg>+41 41 555 01 20</div>
    <div><svg width="8" height="8" aria-hidden="true"><circle cx="4" cy="4" r="4" fill="var(--orange)"/><rect x="2" y="2.7" width="4" height="2.8" fill="none" stroke="#fff" stroke-width=".8"/></svg>sales@netaris.ch</div>
    <div><svg width="8" height="8" aria-hidden="true"><circle cx="4" cy="4" r="4" fill="var(--orange)"/><circle cx="4" cy="4" r="2" fill="none" stroke="#fff" stroke-width=".8"/></svg>www.netaris.ch</div>
  </div>
  <div class="contact" style="left:196px;top:459px;line-height:13px">
    <div style="align-items:flex-start"><svg width="8" height="10" style="margin-top:2px" aria-hidden="true"><path d="M4 10 C1 6 0 5 0 3.6 A4 4 0 0 1 8 3.6 C8 5 7 6 4 10Z" fill="var(--orange)"/><circle cx="4" cy="3.8" r="1.4" fill="var(--teal)"/></svg><span>Netaris AG<br>Lindenweg 12<br>6300 Zug</span></div>
  </div>
</section>

</body>
</html>
```